Homescreen design for android application

We are building android and IOS application.
Idea behind 'WidgetKLM' is to create some kind of mashup between Flirvo and e-commerce site without money being included, items would be swapped for other things.
There are many other interesting features&ideas that could and maybe will be implemented on the basic concept (mostly monetary based stuff),
but for start we would like to get initial thoughts and design vision for home screen based upon provided description.
We would like to avoid corporate look&design, rather some kind of light and friendly interface using light cheerful colors (white, orange, purple etc.).
Home screen requirements:
- Logo
- Headline section (e.g. 'If you're trying to get something new but not ready to spend any money....')
- Info/Warning message (e.g. 'Please verify your account via link sent to your email: moonpilot@[url removed, login to view]')
- Item photo display with its name and description (e.g. photo + "Item #1" + "This item is...")
- Item photo section should have functionality to expand description of photo (e.g. slide out over a photo or something)
- Item photo when swipe will have some king of animation (e.g. fading, sliding out of focus)
- Selection for user added items (maybe something like snapgrove live story circles)
- Quick link icons (PairBox/TopPicks/UserProfile)
Please try to be creative with icons, for PairBox some icon where are really real life matches as an icon and stuff like that.
TopPicks icon should be emphasized (e.g. via border or icon color) in some way to attract attention from users.
- Contact us icon/link or something smoother.

Be open minded, we're ready for something fun and different!

We have 6 more screens to design so if you do well on this screen we will probably hire you to design the rest of the app.

UPDATE:
I added mockup of our idea for the screen design. We don't want you to strictly do it as shown in mockup, we want you to be creative and create the best you can from mockup. You are free to implement your ideas, mockup is just a little help for you

```html
<!DOCTYPE html>
<html lang="en">
<head>
<meta charset="utf-8">
<title>WidgetKLM – Home Screen</title>
<link href="https://fonts.googleapis.com/css2?family=Roboto:wght@400;500;700&family=Montserrat:wght@500&family=Pacifico&display=swap" rel="stylesheet">
<style>
  :root {
    --orange: #e8633f;
    --orange-dark: #d2532f;
    --coral: #e85a4f;
    --alert-red: #e2404f;
    --blue: #3159bb;
    --purple: #7438b5;
    --white: #ffffff;
    --tab-grey: #f1f2f5;
    --text-dark: #333338;
    --text-mute: #7a7a82;
    --icon-grey: #a9abb3;
    --frame-dark: #1e1e22;
  }
  * { box-sizing: border-box; margin: 0; padding: 0; }
  html, body { width: 1200px; height: 2329px; overflow: hidden; background: var(--white); }
  body { position: relative; font-family: "Roboto", sans-serif; }

  /* presentation labels */
  .scroll-hint { position: absolute; left: 78px; top: 293px; width: 28px; height: 270px; }
  .scroll-hint span {
    position: absolute; left: 50%; top: 50%;
    transform: translate(-50%, -50%) rotate(-90deg);
    white-space: nowrap; font-family: "Montserrat", sans-serif; font-weight: 500;
    font-size: 19px; letter-spacing: 7px; color: var(--coral);
  }
  .scroll-arrow { position: absolute; left: 78px; top: 590px; }
  .script-title {
    position: absolute; font-family: "Pacifico", cursive; color: var(--coral);
    font-size: 78px; font-weight: 400; line-height: 1; white-space: nowrap;
  }
  .title-pixel { left: 153px; top: 1520px; }
  .title-tab { left: 767px; top: 2088px; }

  /* brand band */
  .brand-band {
    position: absolute; left: 549px; top: 153px; width: 651px; height: 586px;
    background: linear-gradient(180deg, var(--blue) 0%, var(--purple) 100%);
  }
  .brand-band .band-top {
    height: 74px;
    background: linear-gradient(180deg, var(--orange-dark) 0 20px, var(--orange) 20px);
  }
  .brand-band .brand-name {
    position: absolute; left: 0; right: 0; top: 275px; text-align: center;
    font-size: 68px; font-weight: 700; color: var(--white); letter-spacing: 1px;
  }

  /* app screen */
  .screen {
    position: absolute; left: 220px; top: 153px; width: 329px; height: 586px;
    overflow: hidden;
    background: linear-gradient(180deg, var(--blue) 0%, var(--purple) 100%);
    box-shadow: 0 10px 30px rgba(40, 30, 80, .25);
  }
  .status-bar {
    height: 20px; background: var(--orange-dark); color: var(--white);
    font-size: 10px; display: flex; justify-content: flex-end; align-items: center;
    gap: 6px; padding-right: 6px;
  }
  .app-bar {
    height: 53px; background: var(--orange); position: relative;
    display: flex; align-items: center; justify-content: center;
  }
  .app-bar .app-logo { color: var(--white); font-size: 22px; font-weight: 700; }
  .app-bar .menu-icon { position: absolute; left: 16px; top: 17px; }
  .app-bar .cart-icon { position: absolute; right: 16px; top: 14px; }

  .alert {
    position: absolute; left: 17px; top: 84px; width: 295px; height: 64px;
    background: var(--alert-red); color: var(--white);
    font-size: 9.5px; line-height: 15px; padding: 16px 48px 0 18px;
  }
  .alert .close-icon { position: absolute; right: 14px; top: 18px; }

  .thumbs { position: absolute; left: 0; top: 163px; width: 100%; height: 60px; }
  .thumb { position: absolute; top: 0; width: 43px; }
  .thumb .thumb-photo {
    width: 43px; height: 43px; border-radius: 5px; border: 2px solid rgba(255,255,255,.5);
  }
  .thumb.is-active .thumb-photo { border: 3px solid var(--white); }
  .thumb .thumb-label {
    display: block; text-align: center; font-size: 8px; color: rgba(255,255,255,.7); margin-top: 3px;
  }
  .thumb.is-active .thumb-label { color: var(--white); font-weight: 700; }
  .shade-stripes { background: linear-gradient(180deg, #d9dfe8, #3c4e72 50%, #e6e9ef); }
  .shade-bag { background: linear-gradient(160deg, #5b5d60, #e9e2d2 60%, #7d8088); }
  .shade-shoes { background: linear-gradient(160deg, #c7a46a, #7a5a33 60%, #e2d8c4); }
  .shade-wallet { background: linear-gradient(160deg, #c0703c, #8a4a26); }
  .shade-leather { background: linear-gradient(160deg, #6f5a48, #a8794f); }
  .shade-rack { background: linear-gradient(150deg, #2f2f33 0%, #e3c69a 40%, #1c8a5b 75%, #3a3f44 100%); }

  .card-stack {
    position: absolute; left: 53px; top: 243px; width: 222px; height: 30px;
    background: rgba(255,255,255,.25);
  }
  .card {
    position: absolute; left: 44px; top: 253px; width: 240px; height: 256px;
    background: var(--white);
  }
  .card .card-photo {
    position: absolute; left: 0; top: 0; width: 240px; height: 182px;
    clip-path: polygon(0 0, 100% 0, 100% 78%, 0 100%);
  }
  .card .info-icon { position: absolute; left: 9px; top: 8px; }
  .card .share-btn { position: absolute; left: 186px; top: 117px; }
  .card .item-name {
    position: absolute; left: 18px; top: 188px; font-size: 17px; font-weight: 500; color: var(--coral);
  }
  .card .item-desc {
    position: absolute; left: 18px; top: 211px; width: 210px;
    font-size: 10.5px; line-height: 13px; color: var(--text-dark);
  }

  .tab-bar { position: absolute; background: var(--tab-grey); }
  .tab-bar .tab { position: absolute; top: 0; text-align: center; color: var(--text-mute); }
  .tab-bar .tab-label { display: block; white-space: nowrap; }
  .tab-bar .heart-btn { position: absolute; }

  .screen .tab-bar { left: 0; top: 536px; width: 329px; height: 50px; }
  .screen .tab-bar .tab { width: 80px; padding-top: 8px; }
  .screen .tab-bar .tab-label { font-size: 7.5px; margin-top: 1px; }
  .screen .tab-bar .tab-top { left: 44px; }
  .screen .tab-bar .tab-profile { left: 207px; }
  .screen .tab-bar .heart-btn { left: 141px; top: -14px; }

  .tab-bar.is-large { left: 147px; width: 516px; height: 76px; }
  .tab-bar.is-large .tab { width: 140px; padding-top: 14px; }
  .tab-bar.is-large .tab-label { font-size: 13px; margin-top: 4px; color: var(--text-dark); }
  .tab-bar.is-large .tab-top { left: 60px; }
  .tab-bar.is-large .tab-profile { left: 314px; }
  .tab-bar.is-large .heart-btn { left: 219px; top: -40px; }
  .tab-state-idle { top: 1907px; }
  .tab-state-active { top: 2107px; }

  /* detail zoom: soft-focus screen with magnifier */
  .soft-screen {
    position: absolute; left: 722px; top: 1027px; width: 333px; height: 580px;
    background: linear-gradient(180deg, var(--blue) 0%, var(--purple) 100%);
    filter: blur(6px); overflow: hidden;
  }
  .soft-screen > div { position: absolute; }
  .soft-screen .s-bar { left: 0; top: 0; width: 100%; height: 72px; background: var(--orange); }
  .soft-screen .s-alert { left: 17px; top: 84px; width: 297px; height: 64px; background: var(--alert-red); }
  .soft-screen .s-thumb { top: 163px; width: 43px; height: 43px; border-radius: 5px; }
  .soft-screen .s-card { left: 44px; top: 253px; width: 242px; height: 255px; background: var(--white); }
  .soft-screen .s-photo { left: 44px; top: 253px; width: 242px; height: 182px; clip-path: polygon(0 0, 100% 0, 100% 78%, 0 100%); }
  .soft-screen .s-name { left: 62px; top: 446px; width: 80px; height: 12px; background: var(--coral); }
  .soft-screen .s-tabs { left: 0; top: 530px; width: 100%; height: 50px; background: var(--tab-grey); }
  .soft-screen .s-heart { left: 142px; top: 516px; width: 48px; height: 48px; border-radius: 50%; background: var(--white); border: 3px solid var(--coral); }

  .magnifier {
    position: absolute; left: 436px; top: 1070px; width: 394px; height: 394px;
    border-radius: 50%; overflow: hidden; border: 14px solid var(--white);
    box-shadow: 0 22px 40px rgba(0,0,0,.22);
    background: linear-gradient(180deg, var(--blue) 0%, #5a3fbd 100%);
  }
  .magnifier > div { position: absolute; }
  .magnifier .m-side { left: 0; top: 0; width: 92px; height: 100%; background: var(--coral); }
  .magnifier .m-edge { left: 92px; top: 0; width: 30px; height: 100%; background: var(--frame-dark); }
  .magnifier .m-alert {
    left: 152px; top: -10px; width: 300px; height: 62px; background: var(--alert-red);
    color: var(--white); font-size: 18px; padding: 22px 0 0 36px; white-space: nowrap;
  }
  .magnifier .m-thumb { top: 84px; width: 72px; }
  .magnifier .m-thumb .thumb-photo { width: 72px; height: 72px; border-radius: 8px; border: 3px solid rgba(255,255,255,.6); }
  .magnifier .m-thumb .thumb-label { display: block; text-align: center; font-size: 15px; color: rgba(255,255,255,.8); margin-top: 6px; }
  .magnifier .m-stack { left: 225px; top: 202px; width: 200px; height: 40px; background: rgba(255,255,255,.25); }
  .magnifier .m-card { left: 200px; top: 232px; width: 220px; height: 200px; }
  .magnifier .m-info { left: 214px; top: 246px; }
</style>
</head>
<body>

  <div class="scroll-hint"><span>SCROLL DOWN</span></div>
  <svg class="scroll-arrow" width="28" height="40" viewBox="0 0 28 40">
    <path d="M14 2 V36 M3 25 L14 36 L25 25" fill="none" stroke="#e85a4f" stroke-width="3"/>
  </svg>

  <section class="brand-band">
    <div class="band-top"></div>
    <div class="brand-name">WidgetKLM</div>
  </section>

  <section class="screen">
    <div class="status-bar">
      <svg width="20" height="9" viewBox="0 0 20 9"><path d="M0 0 H9 L4.5 8 Z M12 8 L19 0 V8 Z" fill="#fff"/></svg>
      <span>07:53</span>
    </div>
    <header class="app-bar">
      <svg class="menu-icon" width="20" height="16" viewBox="0 0 20 16">
        <path d="M0 2 H20 M0 8 H20 M0 14 H14" stroke="#fff" stroke-width="2"/>
      </svg>
      <span class="app-logo">WidgetKLM</span>
      <svg class="cart-icon" width="24" height="24" viewBox="0 0 24 24">
        <rect x="3" y="6" width="18" height="15" rx="2" fill="none" stroke="#fff" stroke-width="2"/>
        <path d="M8 10 Q12 16 16 10" fill="none" stroke="#fff" stroke-width="2"/>
        <path d="M3 9 H21" stroke="#fff" stroke-width="1.5"/>
      </svg>
    </header>

    <div class="alert">
      Please verify your account via link sent to<br>your email moonpilot@[url removed, login to view]
      <svg class="close-icon" width="28" height="28" viewBox="0 0 28 28">
        <circle cx="14" cy="14" r="12" fill="none" stroke="#b71f32" stroke-width="1.5"/>
        <path d="M9 9 L19 19 M19 9 L9 19" stroke="#b71f32" stroke-width="1.5"/>
      </svg>
    </div>

    <div class="thumbs">
      <div class="thumb" style="left:19px"><div class="thumb-photo shade-stripes" role="img" aria-label="Striped shirt"></div><span class="thumb-label">item#</span></div>
      <div class="thumb" style="left:80px"><div class="thumb-photo shade-bag" role="img" aria-label="Canvas pouch"></div><span class="thumb-label">item#</span></div>
      <div class="thumb is-active" style="left:140px"><div class="thumb-photo shade-shoes" role="img" aria-label="Leather shoes"></div><span class="thumb-label">item#</span></div>
      <div class="thumb" style="left:203px"><div class="thumb-photo shade-wallet" role="img" aria-label="Brown wallet"></div><span class="thumb-label">item#</span></div>
      <div class="thumb" style="left:264px"><div class="thumb-photo shade-leather" role="img" aria-label="Leather bag"></div><span class="thumb-label">item#</span></div>
      <div class="thumb" style="left:325px"><div class="thumb-photo shade-bag" role="img" aria-label="Further item"></div></div>
    </div>

    <div class="card-stack"></div>
    <article class="card">
      <div class="card-photo shade-rack" role="img" aria-label="Clothes hanging on a rail"></div>
      <svg class="info-icon" width="22" height="22" viewBox="0 0 22 22">
        <circle cx="11" cy="11" r="10" fill="#e9e9eb" stroke="#333" stroke-width="1.2"/>
        <circle cx="11" cy="6.5" r="1.5" fill="#222"/>
        <path d="M11 9.5 V16" stroke="#222" stroke-width="2.6"/>
      </svg>
      <svg class="share-btn" width="30" height="30" viewBox="0 0 30 30">
        <circle cx="15" cy="15" r="15" fill="#e8633f"/>
        <path d="M9 20 Q10 13 18 13 V10 L22 14.5 L18 19 V16 Q12 16 9 20 Z" fill="none" stroke="#fff" stroke-width="1.4"/>
      </svg>
      <h2 class="item-name">Item Name</h2>
      <p class="item-desc">This item is lorem ipsum dolar aimet, set aimet. poin gravida, lorem ipsum dolar set aimet lorem ipsum</p>
    </article>

    <nav class="tab-bar">
      <div class="tab tab-top">
        <svg width="12" height="16" viewBox="0 0 12 16"><path d="M7 0 L1 9 H6 L4 16 L11 6 H6 Z" fill="none" stroke="#a9abb3" stroke-width="1"/></svg>
        <span class="tab-label">Top Picks</span>
      </div>
      <svg class="heart-btn" width="48" height="48" viewBox="0 0 48 48">
        <circle cx="24" cy="24" r="22" fill="#fff" stroke="#e8633f" stroke-width="2.5"/>
        <path d="M24 33 L14 22.5 A5.5 5.5 0 0 1 24 16.5 A5.5 5.5 0 0 1 34 22.5 Z" fill="#e85a4f"/>
        <path d="M19 21.5 L24 26.5 L29 21.5" fill="none" stroke="#fff" stroke-width="2.4"/>
      </svg>
      <div class="tab tab-profile">
        <svg width="16" height="16" viewBox="0 0 16 16"><circle cx="8" cy="5" r="4" fill="none" stroke="#a9abb3"/><path d="M1 16 Q1 9.5 8 9.5 Q15 9.5 15 16" fill="none" stroke="#a9abb3"/></svg>
        <span class="tab-label">My Profile</span>
      </div>
    </nav>
  </section>

  <section class="soft-screen" aria-hidden="true">
    <div class="s-bar"></div>
    <div class="s-alert"></div>
    <div class="s-thumb shade-stripes" style="left:19px"></div>
    <div class="s-thumb shade-bag" style="left:80px"></div>
    <div class="s-thumb shade-shoes" style="left:140px"></div>
    <div class="s-thumb shade-wallet" style="left:203px"></div>
    <div class="s-thumb shade-leather" style="left:264px"></div>
    <div class="s-card"></div>
    <div class="s-photo shade-rack"></div>
    <div class="s-name"></div>
    <div class="s-tabs"></div>
    <div class="s-heart"></div>
  </section>

  <section class="magnifier" aria-label="Close-up of the item selector">
    <div class="m-side"></div>
    <div class="m-edge"></div>
    <div class="m-alert">your em</div>
    <div class="m-thumb" style="left:164px"><div class="thumb-photo shade-stripes" role="img" aria-label="Striped shirt"></div><span class="thumb-label">item#</span></div>
    <div class="m-thumb" style="left:268px"><div class="thumb-photo shade-bag" role="img" aria-label="Canvas pouch"></div><span class="thumb-label">item#</span></div>
    <div class="m-stack"></div>
    <div class="m-card shade-rack" role="img" aria-label="Clothes hanging on a rail"></div>
    <svg class="m-info" width="36" height="36" viewBox="0 0 22 22" style="position:absolute">
      <circle cx="11" cy="11" r="10" fill="#e9e9eb" stroke="#333" stroke-width="1.2"/>
      <circle cx="11" cy="6.5" r="1.5" fill="#222"/>
      <path d="M11 9.5 V16" stroke="#222" stroke-width="2.6"/>
    </svg>
  </section>

  <h1 class="script-title title-pixel">Pixel Perfect</h1>

  <nav class="tab-bar is-large tab-state-idle">
    <div class="tab tab-top">
      <svg width="18" height="26" viewBox="0 0 18 26"><path d="M11 1 L2 15 H9 L6 25 L16 10 H9 Z" fill="none" stroke="#a9abb3" stroke-width="1.2"/></svg>
      <span class="tab-label">Top Picks</span>
    </div>
    <svg class="heart-btn" width="80" height="80" viewBox="0 0 48 48">
      <circle cx="24" cy="24" r="22" fill="#fff" stroke="#e8633f" stroke-width="2"/>
      <path d="M24 33 L14 22.5 A5.5 5.5 0 0 1 24 16.5 A5.5 5.5 0 0 1 34 22.5 Z" fill="#e85a4f"/>
      <path d="M19 21.5 L24 26.5 L29 21.5" fill="none" stroke="#fff" stroke-width="2.4"/>
    </svg>
    <div class="tab tab-profile">
      <svg width="26" height="26" viewBox="0 0 16 16"><circle cx="8" cy="5" r="4" fill="none" stroke="#a9abb3" stroke-width=".8"/><path d="M1 16 Q1 9.5 8 9.5 Q15 9.5 15 16" fill="none" stroke="#a9abb3" stroke-width=".8"/></svg>
      <span class="tab-label">My Profile</span>
    </div>
  </nav>

  <nav class="tab-bar is-large tab-state-active">
    <div class="tab tab-top">
      <svg width="18" height="26" viewBox="0 0 18 26"><path d="M11 1 L2 15 H9 L6 25 L16 10 H9 Z" fill="#e8633f"/></svg>
      <span class="tab-label">Top Picks</span>
    </div>
    <svg class="heart-btn" width="80" height="80" viewBox="0 0 48 48">
      <circle cx="24" cy="24" r="22" fill="#fff" stroke="#e8633f" stroke-width="2"/>
      <path d="M24 33 L14 22.5 A5.5 5.5 0 0 1 24 16.5 A5.5 5.5 0 0 1 34 22.5 Z" fill="#e85a4f"/>
      <path d="M19 21.5 L24 26.5 L29 21.5" fill="none" stroke="#fff" stroke-width="2.4"/>
    </svg>
    <div class="tab tab-profile">
      <svg width="26" height="26" viewBox="0 0 16 16"><circle cx="8" cy="5" r="4" fill="#e8633f"/><path d="M1 16 Q1 9.5 8 9.5 Q15 9.5 15 16 Z" fill="#e8633f"/></svg>
      <span class="tab-label">My Profile</span>
    </div>
  </nav>

  <h1 class="script-title title-tab">Tab Bar</h1>

</body>
</html>
```